ReDesign Website for a more Bold approach

Hello! I'd like to redesign my website: holvencrest.com

I'd like to add one thing that's not on my website which is a blog. The design around the blog should be put time into as I will be putting out incredibly great content and want it to attract viewers.

I get a lot of inspiration from ruvtal.com (the way they flow the big statements across each screen, colors)
moorlane.vc (the simplicity behind the design is beautiful)

I like modern very simple but bold approaches.

I am going to attach my logo here and if it can be thought of when making the design of the website. Thanks!

Industry/Entity Type

Finance and Private Equity

Number of Pages Required

3 page

Font styles to use
Serif
Sans Serif

Colors
0054AA
0677BA
7BADD7
CADEEF
E8F1F8
0094D4
00A9DD
6FCCEA
C7EBF8
E9F6FB
00AB8E
00BBA5
67D7C9
C6EFE9
E9F9F6

Requirements
Must have
• My project must have a Home, Expertise, Story, Clients, Approach, Blog, Contact
Nice to have
• It would be nice to have these tabs reduced to 1-3 pages
Should not have
• My project must not have bright colors.

```html
<!DOCTYPE html>
<html lang="en">
<head>
<meta charset="utf-8">
<title>Holvencrest Ventures</title>
<link rel="stylesheet" href="https://fonts.googleapis.com/css2?family=Playfair+Display:wght@400&family=Mulish:wght@400;600;700;800&display=swap">
<style>
:root{
  --navy:#0f2640;
  --blue-deep:#0054AA;
  --blue:#0677BA;
  --blue-mid:#3a7cc2;
  --blue-soft:#7BADD7;
  --blue-pale:#E8F1F8;
  --sky:#00A9DD;
  --sky-light:#6FCCEA;
  --sky-btn:#2fb3e3;
  --teal:#00BBA5;
  --teal-dark:#00AB8E;
  --teal-band:#33bfa6;
  --teal-light:#67D7C9;
  --teal-cta:#7de6d8;
  --title-blue:#1f6fa8;
  --text:#3c3f44;
  --muted:#8aa6c4;
  --white:#ffffff;
}
*{box-sizing:border-box;margin:0;padding:0}
html,body{width:1200px;height:3900px;overflow:hidden;background:var(--white)}
body{font-family:'Mulish',sans-serif;color:var(--text);position:relative}
.serif{font-family:'Playfair Display',serif;font-weight:400}
section,header,footer{position:absolute;left:0;width:1200px}
.abs{position:absolute}
.center{text-align:center;left:0;width:1200px}

/* nav */
.site-nav{top:0;height:68px;background:var(--navy)}
.brand{left:87px;top:23px;font-family:'Mulish',sans-serif;font-weight:800;font-size:19px;color:var(--white);letter-spacing:.3px}
.menu{right:88px;top:25px;display:flex;gap:50px;font-size:13px;color:var(--white);font-weight:600}

/* hero */
.hero{top:68px;height:474px;background:linear-gradient(180deg,#1e6fb8 0%,#2d79bd 55%,#4a88c2 100%)}
.hero-photo{position:absolute;inset:0}
.hero-kicker{top:150px;font-size:21px;color:var(--teal-light)}
.hero-title{top:183px;font-size:46px;line-height:53px;color:var(--white)}
.cta{font-weight:800;color:var(--teal-cta);border-bottom:3px solid var(--teal);padding-bottom:1px}
.hero-cta{top:340px;font-size:21px}

/* stats */
.stats{top:542px;height:293px;background:var(--teal)}
.stat{position:absolute;top:67px;width:260px;text-align:center;color:var(--white)}
.stat svg{display:block;margin:0 auto 14px}
.stat-num{font-size:40px;font-weight:800;line-height:42px}
.stat-label{font-size:17px;font-weight:600;margin-top:2px}

/* expertise */
.expertise{top:835px;height:528px}
.exp-panel{left:0;top:0;width:496px;height:528px;background:var(--blue-pale)}
.exp-title{left:176px;top:182px;font-size:52px;line-height:58px;color:var(--title-blue)}
.exp-item{width:245px}
.exp-item h3{font-size:15px;font-weight:800;color:var(--blue);letter-spacing:.3px;margin-bottom:10px;white-space:nowrap}
.exp-item p{font-size:13px;line-height:23px;color:var(--text)}

/* who we are */
.story{top:1363px;height:528px;background:linear-gradient(135deg,#6f9bcb 0%,#86b0da 50%,#9cc0e2 100%)}
.story-title{top:55px;font-size:50px;color:var(--white)}
.story-text{left:129px;width:942px;top:155px;font-size:13px;line-height:23px;color:var(--white)}
.story-text p{margin-bottom:23px}
.story-cta{top:436px;font-size:21px}

/* approach */
.approach{top:1891px;height:527px}
.appr-panel{left:705px;top:0;width:495px;height:527px;background:var(--blue-pale)}
.appr-title{left:823px;top:200px;font-size:52px;line-height:58px;color:var(--title-blue)}
.appr-text{left:86px;top:60px;width:530px;font-size:13px;line-height:23px}
.appr-text p{margin-bottom:23px}
.appr-cta{font-size:21px;font-weight:800;color:var(--blue);border-bottom:3px solid var(--sky-light);display:inline-block}

/* clients */
.clients{top:2418px;height:354px;background:var(--teal-band)}
.clients-title{top:55px;font-size:50px;color:var(--white)}
.logo-row{left:85px;width:1030px;display:flex;justify-content:space-between;align-items:center}
.client{display:flex;align-items:center;gap:7px;font-size:21px;font-weight:700;color:var(--white);width:130px;justify-content:center;white-space:nowrap}
.client i{display:block;width:14px;height:14px;border-radius:50%;background:var(--white);flex:none}

/* news */
.news{top:2772px;height:430px}
.news-title{top:52px;font-size:50px;color:var(--title-blue)}
.post{top:140px;width:325px}
.post h3{font-size:17px;line-height:21px;font-weight:600;color:var(--sky)}
.post .meta{font-size:12px;color:var(--muted);margin:17px 0 15px;display:flex;gap:30px}
.post p{font-size:13px;line-height:23px}
.post .more{display:inline-block;margin-top:4px;font-size:15px;color:#6d7379;border-bottom:3px solid var(--teal-light);line-height:16px;margin-left:4px}

/* newsletter */
.newsletter{top:3202px;height:237px;background:var(--blue-soft)}
.nl-title{top:42px;font-size:34px;color:var(--white)}
.nl-sub{top:84px;font-size:26px;color:var(--blue-pale)}
.field{background:var(--white);border:1px solid #d6e3ef;border-radius:2px;font-size:15px;color:#9bb3cb;padding:8px 10px}
.nl-input{left:380px;top:149px;width:343px;height:35px}
.btn{display:flex;align-items:center;justify-content:center;color:var(--white);font-size:15px;border-radius:2px}
.nl-btn{left:732px;top:149px;width:88px;height:35px;background:var(--blue-mid)}

/* build with us */
.contact{top:3439px;height:461px;background:#3476c0}
.ct-title{top:55px;font-size:50px;color:#8ed2f2}
.ct-lead{top:133px;font-size:13px;line-height:23px;color:var(--white)}
.ct-field{left:262px;width:325px;height:35px}
.ct-area{left:613px;top:198px;width:325px;height:89px}
.ct-btn{left:613px;top:310px;width:187px;height:35px;background:var(--sky-btn)}
.rule{left:236px;top:389px;width:726px;height:1px;background:#6f9fd6}
.copy{left:262px;top:420px;font-size:13px;color:#9fc0e4}
.social{left:836px;top:415px;display:flex;gap:11px}
.social i{display:block;width:26px;height:26px;border-radius:50%;background:#7ba6d8}
</style>
</head>
<body>

<header class="site-nav">
  <div class="abs brand">HOLVENCREST VENTURES</div>
  <nav class="abs menu"><span>HOME</span><span>ABOUT US</span><span>CONTACT</span></nav>
</header>

<section class="hero">
  <div class="hero-photo" role="img" aria-label="City skyline with construction cranes tinted in blue"></div>
  <p class="abs center hero-kicker">Holvencrest Ventures is a venture capital studio firm</p>
  <h1 class="abs center serif hero-title">Raising solid capital for startups and<br>helping businesses jumpstart their revenue</h1>
  <div class="abs center hero-cta"><span class="cta">Find Out More</span></div>
  <svg class="abs" style="left:586px;top:400px" width="28" height="20" viewBox="0 0 28 20"><path d="M3 4 L14 15 L25 4" fill="none" stroke="#fff" stroke-width="4" stroke-linecap="round" stroke-linejoin="round"/></svg>
</section>

<section class="stats">
  <div class="stat" style="left:74px">
    <svg width="72" height="72" viewBox="0 0 72 72" fill="none" stroke="#fff" stroke-width="2.5" stroke-linejoin="round"><path d="M26 10 h18 l-4 10 h-10z"/><path d="M29 20 C12 28 8 60 22 64 h22 C58 60 56 30 41 20"/><text x="35" y="52" fill="#fff" stroke="none" font-size="22" font-family="Mulish,sans-serif" text-anchor="middle">$</text><rect x="46" y="42" width="20" height="5" rx="2"/><rect x="46" y="49" width="20" height="5" rx="2"/><rect x="46" y="56" width="20" height="5" rx="2"/></svg>
    <div class="stat-num">$40M+</div><div class="stat-label">MONEY RAISED</div>
  </div>
  <div class="stat" style="left:339px">
    <svg width="72" height="72" viewBox="0 0 72 72" fill="none" stroke="#fff" stroke-width="2.5" stroke-linejoin="round"><circle cx="20" cy="18" r="12"/><text x="20" y="25" fill="#fff" stroke="none" font-size="18" font-family="Mulish,sans-serif" text-anchor="middle">$</text><rect x="16" y="52" width="8" height="16"/><rect x="28" y="44" width="8" height="24"/><rect x="40" y="34" width="8" height="34"/><rect x="52" y="22" width="8" height="46"/><path d="M14 44 L36 26 L44 32 L64 8"/><path d="M56 8 h8 v8"/></svg>
    <div class="stat-num">$125M+</div><div class="stat-label">ATTRIBUTED REVENUE</div>
  </div>
  <div class="stat" style="left:604px">
    <svg width="72" height="72" viewBox="0 0 72 72" fill="none" stroke="#fff" stroke-width="2.5" stroke-linejoin="round" stroke-linecap="round"><path d="M4 24 l12 -6 l10 16 l-10 6z"/><path d="M68 24 l-12 -6 l-10 16 l10 6z"/><path d="M22 22 l12 -4 l12 6 l-10 6 l-6 -2"/><path d="M20 38 l14 14 a3 3 0 0 0 5 -4 l4 4 a3 3 0 0 0 5 -4 l2 2 a3 3 0 0 0 4 -5 l-6 -9"/></svg>
    <div class="stat-num">11</div><div class="stat-label">COMPANY EXITS</div>
  </div>
  <div class="stat" style="left:860px">
    <svg width="72" height="72" viewBox="0 0 72 72" fill="none" stroke="#fff" stroke-width="2.5" stroke-linejoin="round"><path d="M22 6 h28 v18 a14 14 0 0 1 -28 0z"/><path d="M22 12 h-10 c0 12 6 18 12 18"/><path d="M50 12 h10 c0 12 -6 18 -12 18"/><path d="M36 14 l3 6 l6 1 l-4.5 4 l1 6 l-5.5 -3 l-5.5 3 l1 -6 l-4.5 -4 l6 -1z"/><path d="M33 38 h6 v12 h-6z"/><rect x="24" y="50" width="24" height="8"/><rect x="20" y="58" width="32" height="6"/></svg>
    <div class="stat-num">2</div><div class="stat-label">AWARDS WON</div>
  </div>
</section>

<section class="expertise">
  <div class="abs exp-panel"></div>
  <h2 class="abs serif exp-title">Area of<br>Expertise</h2>
  <div class="abs exp-item" style="left:588px;top:53px"><h3>NETWORK SUPPORT</h3><p>Help you build your network, introducing you to the right people in the right places.</p></div>
  <div class="abs exp-item" style="left:880px;top:53px"><h3>REVENUE ACCELERATION</h3><p>Analyze your revenue streams, providing solutions for kickstarting your revenue</p></div>
  <div class="abs exp-item" style="left:588px;top:218px"><h3>MERGERS &amp; ACQUSITIONS</h3><p>Facilitate a smooth mergers and acquisition process for the expansion of your business</p></div>
  <div class="abs exp-item" style="left:878px;top:218px"><h3>INTEGRATION &amp; INCUBATION</h3><p>Providing training and guidance for startups looking to make their mark on the world.</p></div>
  <div class="abs exp-item" style="left:596px;top:376px"><h3>RAISING CAPITAL</h3><p style="margin-left:-7px">Reach out to our extensive connections to raise vital capital for your startup.</p></div>
  <div class="abs exp-item" style="left:882px;top:376px"><h3>MARKETING</h3><p style="margin-left:-2px">Consult on marketing process, strategies and implementation across your startup.</p></div>
</section>

<section class="story" role="img" aria-label="Team reviewing documents at a desk with a laptop, tinted light blue">
  <h2 class="abs center serif story-title">Who We Are</h2>
  <div class="abs story-text">
    <p>Holvencrest Ventures is a venture capital studio firm based in Austin TX with a laser focus on raising solid capital for startups and helping businesses jumpstart their revenue.</p>
    <p>Founded in 2020 by investment expert Marcus Holven, Holvencrest Ventures combines proven experience in the venture capital field with a data-driven business analysis strategy to secure capital and reinforce revenue streams for startups and established businesses. Born from the idea that the best way to help founders thrive is to understand their strengths, their weaknesses, their ambitions and their needs - our specialists have been through the entire startup process themselves, and that experience forms our unique approach to business support.</p>
    <p>Marcus's work in the sector has seen him take on the biggest and the best, working with iconic business figures to leave an indelible mark on the U.S. startup scene. He brings all of that expertise to the table at Holvencrest Ventures, leading a dedicated team to support the finest international businesses to reach, break through and go beyond their potential.</p>
  </div>
  <div class="abs center story-cta"><span class="cta">Let's Work Together</span></div>
</section>

<section class="approach">
  <div class="abs appr-panel"></div>
  <h2 class="abs serif appr-title">Our<br>Approach</h2>
  <div class="abs appr-text">
    <p>We've built our approach to helping your startup thrive based around three key developmental pillars that guarantee results for our partners.</p>
    <p>First pillar is expertise. We've built our firm on a bank of insights, knowledge and proficiencies honed over years of working with the biggest names in venture capitalism – that experience forms the backbone of every project, every pitch and every investment.</p>
    <p>Second pillar is collaboration. We believe that the best partnerships start with a combined and cooperative approach that benefits all parties every step of the way. We'll always keep our partners up-to-date with our work using regular touchpoints and reports.</p>
    <p>Third and final pillar is trust. We know that our clients and our partners know their industry better than we do, so we trust their input and their ideas – pairing them up with our own business intelligence to guarantee success.</p>
    <span class="appr-cta">Build With Us</span>
  </div>
</section>

<section class="clients">
  <h2 class="abs center serif clients-title">Our Clients</h2>
  <div class="abs logo-row" style="top:157px">
    <div class="client"><i></i>Norvale</div>
    <div class="client">Plumora</div>
    <div class="client"><i></i>Tessaline</div>
    <div class="client">Orbitan</div>
    <div class="client"><i></i>Genlumo</div>
    <div class="client">Kestro</div>
    <div class="client">Vantelle</div>
  </div>
  <div class="abs logo-row" style="top:246px">
    <div class="client"><i></i>Quorix</div>
    <div class="client"><i></i>Lexbridge</div>
    <div class="client">Finwell</div>
    <div class="client"><i></i>Corvana</div>
    <div class="client">Zendri</div>
    <div class="client">Pathmoor</div>
    <div class="client">Estavio<i></i></div>
  </div>
</section>

<section class="news">
  <h2 class="abs center serif news-title">Latest News</h2>
  <article class="abs post" style="left:85px"><h3>We've built our firm on a bank of insights, knowledge and proficiencies</h3><div class="meta"><span>10.12.2021</span><span>Auther Name</span></div><p>Aenean imperdiet. Etiam ultricies nisi vel augue. Curabitur ullamcorper ultricies nisi. Nam eget dui. Etiam rhoncus. Maecenas tempus, tellus eget condimentum rhoncus, sem quam semper libero,</p><span class="more">Read more</span></article>
  <article class="abs post" style="left:439px"><h3>We believe that the best partnerships start with a combined and cooperative</h3><div class="meta"><span>10.12.2021</span><span>Auther Name</span></div><p>Aenean imperdiet. Etiam ultricies nisi vel augue. Curabitur ullamcorper ultricies nisi. Nam eget dui. Etiam rhoncus. Maecenas tempus, tellus eget condimentum rhoncus, sem quam semper libero,</p><span class="more">Read more</span></article>
  <article class="abs post" style="left:788px"><h3>We know that our clients and our partners know their industry better</h3><div class="meta"><span>10.12.2021</span><span>Auther Name</span></div><p>Aenean imperdiet. Etiam ultricies nisi vel augue. Curabitur ullamcorper ultricies nisi. Nam eget dui. Etiam rhoncus. Maecenas tempus, tellus eget condimentum rhoncus, sem quam semper libero,</p><span class="more">Read more</span></article>
</section>

<section class="newsletter">
  <h2 class="abs center serif nl-title">Want to get up to date news?</h2>
  <p class="abs center serif nl-sub">Subscribe to Our Newsletter</p>
  <div class="abs field nl-input">Your email</div>
  <div class="abs btn nl-btn">SIGN UP</div>
</section>

<footer class="contact">
  <h2 class="abs center serif ct-title">Build With Us</h2>
  <p class="abs center ct-lead">Please fill out the form to share your details and SUBMIT.<br>One of our representative will get back to you.</p>
  <div class="abs field ct-field" style="top:198px">Your name</div>
  <div class="abs field ct-field" style="top:253px">Your email</div>
  <div class="abs field ct-field" style="top:308px">Your phone</div>
  <div class="abs field ct-area"></div>
  <div class="abs btn ct-btn">SUBMIT</div>
  <div class="abs rule"></div>
  <p class="abs copy">Copyright © 2022 Holvencrest Ventures.</p>
  <div class="abs social"><i></i><i></i><i></i></div>
</footer>

</body>
</html>
```